Industrial automation company needs new business cards

We need a new business card designed. We have an existing logo that is very simple and are happy to consider changes to it. We have been in business for more than 10 years and our logo has some brand recognition.
We are a company of engineers and build systems for industrial automation, substation automation, power and energy monitoring and production data vertical integration. Our main clients are food manufacturers, data centers and government establishments.
Our current business cards have our name, qualifications, job title, telephone, email and web address details. We don't need our physical address on our business cards. I've attached our current logo

Industry/Entity Type

Business

Logo Text

vardo

Font styles to use
Sans Serif

Colors
6b449b

Requirements
Must have
• - double sided business cards
• - name (eg Mara Quill)
• - qualifications (BE Elec MAGSO)
• - job title (eg Senior Engineer)
• - telephone (eg 0472 518 396)
• - email (eg mara.quill@vardo.com.au)
• - web address (eg vardo.com.au)
Nice to have
• include our target markets on the back side of the card
• - industrial automation
• - substation automation
• - power and energy monitoring
• - production data vertical integration

```html
<!DOCTYPE html>
<html lang="en">
<head>
<meta charset="utf-8">
<title>Vardo business card</title>
<link rel="stylesheet" href="https://fonts.googleapis.com/css2?family=Arimo:wght@400;700&display=swap">
<style>
  :root {
    --page: #f4f4f4;
    --stage: #e3e3e5;
    --ink-grey: #555555;
    --ink-soft: #6b6b6b;
    --violet: #7a00d6;
    --violet-deep: #6400b4;
    --violet-bright: #8c10ee;
    --paper: #efece2;
    --rule: #c9c4b4;
    --white: #ffffff;
  }
  * { box-sizing: border-box; margin: 0; padding: 0; }
  html, body { width: 1200px; height: 1120px; overflow: hidden; }
  body {
    font-family: "Arimo", Arial, sans-serif;
    background: var(--page);
  }
  .brand-panel {
    height: 344px;
    display: flex;
    align-items: center;
    justify-content: center;
    background: var(--page);
  }
  .brand-lockup {
    display: flex;
    align-items: center;
    gap: 16px;
  }
  .brand-square {
    width: 30px;
    height: 30px;
    background: var(--violet);
  }
  .brand-name {
    font-weight: 700;
    font-size: 52px;
    letter-spacing: 8px;
    color: var(--ink-grey);
    text-transform: uppercase;
  }
  .card-stage {
    height: 776px;
    background: var(--stage);
    display: flex;
    align-items: center;
    justify-content: center;
    gap: 60px;
  }
  .card {
    width: 490px;
    height: 280px;
    position: relative;
    box-shadow: 0 6px 18px rgba(0,0,0,0.18);
  }
  .card-front {
    background: var(--paper);
    padding: 34px 36px;
  }
  .holder-name {
    font-weight: 700;
    font-size: 17px;
    color: var(--violet);
    text-transform: uppercase;
    letter-spacing: 0.5px;
  }
  .holder-details {
    margin-top: 6px;
    font-size: 13px;
    line-height: 1.45;
    color: var(--ink-soft);
  }
  .contact-block {
    margin-top: 18px;
    padding-top: 14px;
    border-top: 1px solid var(--rule);
    width: 210px;
    font-size: 13px;
    line-height: 1.55;
    color: var(--ink-soft);
  }
  .front-mark {
    position: absolute;
    right: 36px;
    bottom: 32px;
    display: flex;
    align-items: center;
    gap: 10px;
  }
  .front-mark .brand-square { width: 18px; height: 18px; }
  .front-mark .brand-name { font-size: 28px; letter-spacing: 4px; }
  .card-back {
    background: linear-gradient(135deg, var(--violet-deep) 0%, var(--violet) 50%, var(--violet-bright) 100%);
    display: flex;
    flex-direction: column;
    align-items: center;
    justify-content: center;
    gap: 6px;
  }
  .card-back .brand-name {
    color: var(--white);
    font-size: 34px;
    letter-spacing: 6px;
  }
  .back-url {
    font-size: 13px;
    color: var(--white);
    letter-spacing: 0.5px;
  }
</style>
</head>
<body>
  <header class="brand-panel">
    <div class="brand-lockup">
      <span class="brand-square"></span>
      <span class="brand-name">Vardo</span>
    </div>
  </header>

  <main class="card-stage">
    <section class="card card-front">
      <h1 class="holder-name">Mara Quill</h1>
      <p class="holder-details">BE Elec MAGSO<br>Senior Engineer</p>
      <p class="contact-block">+61 2 5550 1834<br>mara@vardo.com.au<br>www.vardo.com.au</p>
      <div class="front-mark">
        <span class="brand-square"></span>
        <span class="brand-name">Vardo</span>
      </div>
    </section>

    <section class="card card-back">
      <span class="brand-name">Vardo</span>
      <span class="back-url">www.vardo.com.au</span>
    </section>
  </main>
</body>
</html>
```